International Trading Company, 'KIRO' needs a Business Card

The company name is "KIRO" and it has own logo design.
I'd like to use its logo on this business card.
I need two side Business Card.
I'll look forward to your great design.
Thank you very much in advance.

Contact Information for Business Card

Company Name : Kiro Harbour Limited
Information Example
Dorian Pallister
Mobile(use icon please) : 1 (212) 555-0143
Tel(use icon please) : 1 (212) 555-0178
Email(use icon please) : dorian27@kiroharbour-mail.com
Address(use icon please) : 482 Halden Ave, New York, NY 10160, USA

```html
<!DOCTYPE html>
<html lang="en">
<head>
<meta charset="utf-8">
<title>Kiro Harbour Limited — Business Card</title>
<link rel="stylesheet" href="https://fonts.googleapis.com/css2?family=Bebas+Neue&family=PT+Sans:wght@400;700&display=swap">
<style>
  :root {
    --backdrop: #f4d3df;
    --board-light: #6e7175;
    --board-mid: #3a3c3f;
    --board-dark: #141516;
    --band: rgba(22, 23, 25, 0.82);
    --mark-grey: #a3a7ab;
    --title-grey: #b9bcbf;
    --white: #ffffff;
  }
  * { margin: 0; padding: 0; box-sizing: border-box; }
  html, body {
    width: 1200px; height: 1200px; overflow: hidden;
    background: var(--backdrop);
  }
  .card {
    position: absolute;
    left: 240px;
    width: 721px;
    height: 434px;
    overflow: hidden;
  }
  .card--front { top: 105px; }
  .card--back { top: 630px; }
  .card__photo {
    position: absolute; inset: 0;
    background:
      radial-gradient(ellipse at 70% 20%, var(--board-light) 0%, transparent 45%),
      radial-gradient(ellipse at 25% 85%, var(--board-light) 0%, transparent 40%),
      linear-gradient(160deg, var(--board-mid) 0%, var(--board-dark) 55%, var(--board-mid) 100%);
  }
  .card__band {
    position: absolute; left: 0; right: 0;
    background: var(--band);
  }
  .card--front .card__band { top: 78px; height: 271px; }
  .card--back .card__band { top: 83px; height: 261px; }
  .wordmark {
    position: absolute;
    font-family: "Bebas Neue", sans-serif;
    color: var(--mark-grey);
    line-height: 1;
    letter-spacing: 0.04em;
  }
  .card--front .wordmark {
    left: 0; right: 0; top: 150px;
    text-align: center;
    font-size: 120px;
  }
  .card--back .wordmark {
    left: 64px; top: 212px;
    font-size: 70px;
  }
  .company-name {
    position: absolute; left: 0; right: 0; top: 98px;
    text-align: center;
    font-family: "Bebas Neue", sans-serif;
    font-size: 44px;
    color: var(--title-grey);
    letter-spacing: 0.02em;
    line-height: 1;
  }
  .person-name {
    position: absolute; left: 408px; top: 178px;
    font-family: "Bebas Neue", sans-serif;
    font-size: 32px;
    color: var(--white);
    letter-spacing: 0.02em;
    line-height: 1;
  }
  .contact {
    position: absolute; left: 412px; top: 225px;
    font-family: "PT Sans", sans-serif;
    font-size: 16px;
    color: var(--white);
    list-style: none;
    line-height: 22.5px;
  }
  .contact b { font-weight: 700; }
  .contact .label { font-weight: 700; margin-right: 5px; }
</style>
</head>
<body>
  <section class="card card--front">
    <div class="card__photo" role="img" aria-label="Dark monochrome close-up photograph of a computer circuit board"></div>
    <div class="card__band"></div>
    <div class="wordmark">KIRO</div>
  </section>

  <section class="card card--back">
    <div class="card__photo" role="img" aria-label="Dark monochrome close-up photograph of a computer circuit board"></div>
    <div class="card__band"></div>
    <h1 class="company-name">KIRO HARBOUR LIMITED</h1>
    <div class="wordmark">KIRO</div>
    <h2 class="person-name">DORIAN PALLISTER</h2>
    <ul class="contact">
      <li><b>482</b> Halden Ave, New York,</li>
      <li>NY 10160<b>, USA</b></li>
      <li><span class="label">tel:</span> 1 (212) 555-0178</li>
      <li><span class="label">mobil:</span>1 (212) 555-0143</li>
      <li><span class="label">email:</span> dorian27@kiroharbour-mail.com</li>
    </ul>
  </section>
</body>
</html>
```